Business Value Optimisation Consultancy Needs a Web Design

Velor Quintess is a business consultancy in Australia, which assists SMEs (small; to medium sized businesses) to grow revenue signicantly, put in professional operaations, and become worth a lot more as a sale-able business.

It is in need of new website design (you can see the current "old" site here at www.velorquintess.net - please note all content has changed for the new site - please see content file attached).

An example of a site we like is www.bluekestrelhub.com.au because:

a. it is crisp and clear, and quickly conveys what the offering is all about.
b. it offers a report download with email sign up.
c. it is easy and simple to navigate

We don't want an exact copy of this site, but this site is given as an example of the type of clear design we like.

Another example is:

Also, please see the attached powerpoint presentation - please note the style used in it - we would like the website to be close to the powerpoint style but it does not have to be exactly the same.

2. please see attached files with:

a. content for all pages - note the content makes reference to some videos
b. a list of all available videos, as hosted on vimeo
c. blog posts written to date
d. a powerpoint presentation used by Velor Quintess - please keep the site design in line with the style used in this powerpoint presentation.

Designs to be supplied as PSD files.

Thank you!

Target Market(s)

Small to Medium Sized Professional Service Businesses
Technology Start Ups
Medium Businesses Approaching Small Corporate Size

Industry/Entity Type

Business Consultant

Number of Pages Required

3 page

Font styles to use
Sans Serif

Requirements
Must have
• Home Page
• Inner Page
• Blog

```html
<!DOCTYPE html>
<html lang="en">
<head>
<meta charset="utf-8">
<title>Velor Quintess</title>
<link href="https://fonts.googleapis.com/css2?family=Mulish:ital,wght@0,400;0,600;0,700;0,800;1,400&family=Questrial&family=Open+Sans:wght@400;600&display=swap" rel="stylesheet">
<style>
:root{
  --blue:#0aa0dd;
  --blue-text:#1a9fd6;
  --ink:#2f2f2f;
  --grey:#8a8a8a;
  --topbar:#2b2b2b;
  --footer:#2c2c2c;
  --footer-line:#3a3a3a;
  --white:#ffffff;
  --check:#1e9a4a;
  --red:#8e1a1a;
  --head:"Questrial", "Mulish", sans-serif;
  --body:"Open Sans", "Mulish", sans-serif;
}
*{margin:0;padding:0;box-sizing:border-box}
html,body{width:1200px;height:2748px;overflow:hidden}
body{font-family:var(--body);color:var(--ink);background:var(--white);position:relative}
section,header,footer,div{position:relative}
.abs{position:absolute}

/* top bar */
.topbar{height:55px;background:var(--topbar)}
.topbar .social{left:100px;top:19px;display:flex;gap:10px}
.topbar .social span{width:14px;height:14px;background:#d8d8d8;border-radius:2px;display:block}
.topbar .util{right:100px;top:17px;display:flex;gap:28px;font-family:var(--head);font-size:16px;color:#dcdcdc}

/* header */
.site-header{height:119px;background:var(--white)}
.brand{left:100px;top:35px;display:flex;align-items:center;gap:14px}
.brand-mark{width:48px;height:48px;background:var(--blue)}
.brand-name{font-family:var(--head);font-size:23px;color:var(--ink)}
.main-nav{right:100px;top:50px;display:flex;gap:35px;font-family:var(--head);font-size:16px;color:#333}
.main-nav .active{color:var(--blue-text)}

/* hero */
.hero{height:515px;background:linear-gradient(100deg,#4b4f53 0%,#6a6d70 40%,#56595c 70%,#3c3f42 100%)}
.hero h1{position:absolute;left:0;right:0;top:44px;text-align:center;font-family:"Mulish",sans-serif;font-weight:700;font-size:40px;line-height:51px;color:var(--white)}
.hero .pitch{left:100px;top:228px;color:var(--white)}
.hero .pitch .big{font-family:var(--head);font-size:26px;line-height:32px}
.hero .pitch .small{font-size:15.5px;line-height:20px;margin-top:16px}
.video-frame{left:616px;top:187px;width:485px;height:271px;background:var(--white);padding:12px}
.video-frame .still{width:100%;height:100%;background:linear-gradient(180deg,#cfd8e2,#8a98a8 55%,#2c3540)}
.play{position:absolute;width:90px;height:56px;background:var(--red);left:50%;top:50%;transform:translate(-50%,-50%);border-radius:3px;opacity:.92}
.play svg{position:absolute;left:33px;top:16px}

/* intro */
.intro{height:339px}
.intro .lead{position:absolute;left:0;right:0;top:44px;text-align:center;font-family:var(--head);font-size:31px;line-height:40px;color:var(--blue-text)}
.intro h2{left:97px;top:158px;font-family:var(--head);font-weight:400;font-size:27px;color:#333}
.checks{left:97px;top:212px;width:1004px;display:grid;grid-template-columns:445px 560px;row-gap:22px;font-size:12.5px;color:#8a8a8a}
.checks li{list-style:none;display:flex;align-items:center;gap:12px}
.checks svg{flex:none}

/* grow band */
.grow{height:397px;background:var(--blue)}
.grow h2{left:100px;top:105px;font-family:var(--head);font-weight:400;font-size:31px;line-height:37px;color:var(--white)}
.grow ul{left:100px;top:212px;width:480px;display:grid;grid-template-columns:245px 235px;row-gap:16px;list-style:none;font-size:12.5px;line-height:19px;color:var(--white)}
.grow li{display:flex;gap:10px}
.grow li svg{flex:none;margin-top:3px}
.grow .visual{left:621px;top:0;width:579px;height:397px;background:linear-gradient(135deg,#0d1c33,#1f4a78 50%,#0a1628)}

/* learn more */
.learn{height:486px}
.learn h2{position:absolute;left:0;right:0;top:44px;text-align:center;font-family:var(--head);font-weight:400;font-size:34px;color:var(--blue-text)}
.avatar{left:100px;top:169px;width:80px;height:80px;border-radius:50%;background:#7d7a78}
.quote-mark{left:190px;top:162px;font-family:Georgia,serif;font-size:70px;line-height:1;color:#cfcfcf}
.quote{left:198px;top:222px;width:390px;font-size:12.5px;line-height:21px;color:#8a8a8a}
.quote-by{left:198px;top:272px;font-style:italic;font-size:13px;color:#444}
.dots{left:193px;top:322px;display:flex;gap:7px}
.dots span{width:11px;height:11px;border-radius:50%;background:#d9d9d9}
.dots span.on{background:#555}
.learn .video{left:627px;top:130px;width:474px;height:286px;background:linear-gradient(135deg,#3d5466,#7a8e9c 45%,#26333d)}

/* who we are */
.who{height:463px;background:var(--blue)}
.who h2{position:absolute;left:0;right:0;top:50px;text-align:center;font-family:var(--head);font-weight:400;font-size:33px;color:var(--white)}
.cards{left:97px;top:128px;display:flex;gap:31px}
.card{width:315px}
.card .photo{height:150px}
.card h3{font-family:var(--head);font-weight:400;font-size:31px;color:var(--white);margin-top:26px}
.card p{font-size:12px;line-height:21px;color:var(--white);margin-top:12px}

/* footer */
.site-footer{height:312px;background:var(--footer)}
.site-footer h4{font-family:"Mulish",sans-serif;font-weight:800;font-size:19px;color:var(--white);letter-spacing:.3px}
.col{top:52px}
.follow{display:flex;gap:7px;margin-top:20px}
.follow span{width:21px;height:21px;background:#4a8fc7;border-radius:2px}
.news-item{display:flex;gap:14px;margin-top:20px}
.news-item:first-of-type{margin-top:24px}
.thumb{width:92px;height:81px;border:5px solid #444;background:#8a8f96}
.news-item b{display:block;font-family:"Mulish",sans-serif;font-weight:700;font-size:15px;color:#d8d8d8;margin-top:6px}
.news-item small{display:block;font-size:12px;color:#d0d0d0;margin-top:8px}
.links{list-style:none;margin-top:22px;font-size:12.5px;line-height:20.2px;color:#a8a8a8}
.contact p{font-size:12.5px;line-height:20px;color:#a8a8a8;margin-top:22px;width:245px}
.copyright{height:62px;background:var(--footer);border-top:1px solid var(--footer-line);text-align:center;font-size:12.5px;line-height:62px;color:#9a9a9a}
</style>
</head>
<body>

<div class="topbar">
  <div class="abs social"><span></span><span></span><span></span><span></span><span></span></div>
  <nav class="abs util"><span>FAQs</span><span>Blog</span><span>Contact Us</span></nav>
</div>

<header class="site-header">
  <div class="abs brand">
    <div class="brand-mark"></div>
    <div class="brand-name">Velor Quintess</div>
  </div>
  <nav class="abs main-nav">
    <span class="active">Home</span><span>One Stop Solution</span><span>Why It Works</span><span>What We Do</span><span>Case Studies</span><span>About Us</span>
  </nav>
</header>

<section class="hero" role="img" aria-label="Background photograph of business people in a meeting">
  <h1>Forward-thinking strategies to grow your business<br>and optimise its potential</h1>
  <div class="abs pitch">
    <p class="big">You want your business to flourish.<br>But you’re afraid of the potential risk.</p>
    <p class="small">You CAN grow your business with a game-changing<br>strategy. Safely.</p>
  </div>
  <div class="abs video-frame">
    <div class="still" role="img" aria-label="Video still of a smiling business team in suits">
      <div class="play"><svg width="24" height="24" viewBox="0 0 24 24"><path d="M2 0 L24 12 L2 24 Z" fill="#fff"/></svg></div>
    </div>
  </div>
</section>

<section class="intro">
  <p class="lead">We help entrepreneurial businesses reach their true<br>potential and maximise their market value</p>
  <h2 class="abs">Do you recognize your business?</h2>
  <ul class="abs checks">
    <li><svg width="14" height="14" viewBox="0 0 14 14"><rect width="14" height="14" fill="var(--check)"/><path d="M3 7 L6 10 L11 4" stroke="#fff" stroke-width="2" fill="none"/></svg>You have big plans for growth, but aren’t sure how to implement them</li>
    <li><svg width="14" height="14" viewBox="0 0 14 14"><rect width="14" height="14" fill="var(--check)"/><path d="M3 7 L6 10 L11 4" stroke="#fff" stroke-width="2" fill="none"/></svg>You fear the risk and additional capital commitment it would take to grow</li>
    <li><svg width="14" height="14" viewBox="0 0 14 14"><rect width="14" height="14" fill="var(--check)"/><path d="M3 7 L6 10 L11 4" stroke="#fff" stroke-width="2" fill="none"/></svg>You own a successful SME but it has yet to reach it’s full potential</li>
    <li><svg width="14" height="14" viewBox="0 0 14 14"><rect width="14" height="14" fill="var(--check)"/><path d="M3 7 L6 10 L11 4" stroke="#fff" stroke-width="2" fill="none"/></svg>If you sold your business today, you aren’t sure you could get what it’s worth</li>
  </ul>
</section>

<section class="grow">
  <h2 class="abs">Your business grows from good<br>to great when together we:</h2>
  <ul class="abs">
    <li><svg width="11" height="11" viewBox="0 0 11 11"><circle cx="5.5" cy="5.5" r="5.5" fill="#fff"/><path d="M4 3 L7 5.5 L4 8" stroke="var(--blue)" stroke-width="1.6" fill="none"/></svg>Identify the issues holding you back</li>
    <li><svg width="11" height="11" viewBox="0 0 11 11"><circle cx="5.5" cy="5.5" r="5.5" fill="#fff"/><path d="M4 3 L7 5.5 L4 8" stroke="var(--blue)" stroke-width="1.6" fill="none"/></svg>Develop a three-year strategic plan</li>
    <li><svg width="11" height="11" viewBox="0 0 11 11"><circle cx="5.5" cy="5.5" r="5.5" fill="#fff"/><path d="M4 3 L7 5.5 L4 8" stroke="var(--blue)" stroke-width="1.6" fill="none"/></svg>Position your company for stand-out success with the right management, distribution and financial models</li>
    <li><svg width="11" height="11" viewBox="0 0 11 11"><circle cx="5.5" cy="5.5" r="5.5" fill="#fff"/><path d="M4 3 L7 5.5 L4 8" stroke="var(--blue)" stroke-width="1.6" fill="none"/></svg>Optimise your company’s financial value in the marketplace</li>
  </ul>
  <div class="abs visual" role="img" aria-label="Photograph of a businessman drawing a glowing growth chart on a digital screen"></div>
</section>

<section class="learn">
  <h2>Want to learn more?</h2>
  <div class="abs avatar" role="img" aria-label="Portrait photo of a client"></div>
  <div class="abs quote-mark">“</div>
  <p class="abs quote">Neque porro quisquam est qui dolorem ipsum quia dolor sit amet, consectetur, adipisci velit...</p>
  <p class="abs quote-by">Lorem ipsum</p>
  <div class="abs dots"><span class="on"></span><span></span><span></span></div>
  <div class="abs video" role="img" aria-label="Video still of a consultant at a digital display with the word Consulting">
    <div class="play"><svg width="24" height="24" viewBox="0 0 24 24"><path d="M2 0 L24 12 L2 24 Z" fill="#fff"/></svg></div>
  </div>
</section>

<section class="who">
  <h2>Who We Are</h2>
  <div class="abs cards">
    <article class="card">
      <div class="photo" role="img" aria-label="Photo of colleagues working together at a desk" style="background:linear-gradient(135deg,#c9d4e0,#7e8fa3)"></div>
      <h3>What We Do</h3>
      <p>Neque porro quisquam est qui dolorem ipsum quia dolor sit amet, consectetur, adipisci velit...</p>
    </article>
    <article class="card">
      <div class="photo" role="img" aria-label="Photo of a businesswoman with a team behind her" style="background:linear-gradient(135deg,#f1f1f1,#b9bcc2)"></div>
      <h3>Our Vision</h3>
      <p>Neque porro quisquam est qui dolorem ipsum quia dolor sit amet, consectetur, adipisci velit...</p>
    </article>
    <article class="card">
      <div class="photo" role="img" aria-label="Photo of business partners meeting in an office" style="background:linear-gradient(135deg,#d6dbe1,#4c5866)"></div>
      <h3>Who We Work With</h3>
      <p>Neque porro quisquam est qui dolorem ipsum quia dolor sit amet, consectetur, adipisci velit...</p>
    </article>
  </div>
</section>

<footer class="site-footer">
  <div class="abs col" style="left:100px">
    <h4>STAY IN TOUCH</h4>
    <div class="follow"><span></span><span></span><span></span><span></span></div>
  </div>
  <div class="abs col" style="left:330px">
    <h4>LATEST NEWS</h4>
    <div class="news-item"><div class="thumb" role="img" aria-label="News thumbnail of a business meeting"></div><div><b>Lorem ipsum dolor</b><small>Apr 30,2015</small></div></div>
    <div class="news-item"><div class="thumb" role="img" aria-label="News thumbnail of a businessman"></div><div><b>Lorem ipsum dolor</b><small>Apr 30,2015</small></div></div>
  </div>
  <div class="abs col" style="left:656px">
    <h4>QUICK LINKS</h4>
    <ul class="links"><li>Home</li><li>One Stop Solution</li><li>Why It Works</li><li>What We Do</li><li>Case Studies</li><li>About Us</li><li>FAQs</li><li>Blog</li><li>Contact Us</li></ul>
  </div>
  <div class="abs col contact" style="left:863px">
    <h4>CONTACT US</h4>
    <p>Nemo enim ipsam voluptatem quia voluptas sit aspernatur</p>
    <p>1800-555-274<br>hello@velorquintess.net</p>
  </div>
</footer>
<div class="copyright">© Copyright 2015 velorquintess.net</div>

</body>
</html>
```